PELDRAX Business Cards

We require a business card for our company that provides IT consulting services. We already have a logo that needs to be used on the card. We want a clean professional looking design that incorporates our colours. Our main focus is providing managed services to business, which involves us looking after all of their IT requirements including managing servers/networks, projects, and procurement.

Industry/Entity Type

Information Technology

Requirements
Must have
• our logo, contact information, name, title, phone numbers

```html
<!DOCTYPE html>
<html lang="en">
<head>
<meta charset="utf-8">
<title>PELDRAX Business Cards</title>
<link rel="stylesheet" href="https://fonts.googleapis.com/css2?family=Work+Sans:wght@400;500;600&display=swap">
<style>
  :root {
    --brand-blue: #1592cf;
    --brand-blue-light: #63b8e2;
    --card-white: #ffffff;
    --text-dark: #3a3a3a;
    --text-grey: #555555;
    --page-bg: #e9e9e9;
  }
  * { margin: 0; padding: 0; box-sizing: border-box; }
  html, body {
    width: 1200px; height: 960px; overflow: hidden;
    background: var(--page-bg);
    font-family: "Work Sans", Arial, sans-serif;
  }
  .canvas { position: relative; width: 1200px; height: 960px; }
  .card {
    position: absolute; left: 270px; width: 664px; height: 380px;
    overflow: hidden;
  }
  .card-front { top: 72px; background: var(--brand-blue); color: var(--card-white); }
  .card-back { top: 509px; background: var(--card-white); }

  .wordmark {
    display: flex; align-items: center; gap: 14px;
    font-weight: 600; letter-spacing: 2px; line-height: 1;
  }
  .wordmark-dot { border-radius: 50%; flex: none; }

  .card-front .wordmark {
    position: absolute; left: 0; right: 0; top: 170px;
    justify-content: center; font-size: 60px;
  }
  .card-front .wordmark-dot { width: 48px; height: 48px; background: var(--card-white); }
  .front-url {
    position: absolute; left: 0; right: 0; top: 307px;
    text-align: center; font-size: 21px; font-weight: 500; letter-spacing: 0.5px;
  }

  .card-back .wordmark {
    position: absolute; left: 30px; top: 73px;
    font-size: 40px; color: var(--brand-blue); gap: 10px;
  }
  .card-back .wordmark-dot { width: 32px; height: 32px; background: var(--brand-blue); }

  .person { position: absolute; right: 26px; top: 178px; text-align: right; }
  .person-name {
    font-size: 30px; font-weight: 500; letter-spacing: 1.5px;
    color: var(--brand-blue); line-height: 1.1;
  }
  .person-title { font-size: 16px; color: var(--text-grey); margin-top: 2px; letter-spacing: 0.3px; }

  .divider {
    position: absolute; left: 30px; right: 28px; top: 249px;
    height: 1px; background: var(--brand-blue);
  }

  .contact-list { position: absolute; left: 30px; top: 281px; list-style: none; }
  .contact-list li {
    display: flex; align-items: center; gap: 8px;
    font-size: 16px; color: var(--text-dark); height: 21px; letter-spacing: 0.3px;
  }
  .contact-icon { width: 12px; height: 12px; flex: none; }

  .swoosh { position: absolute; left: 0; bottom: 0; width: 664px; height: 380px; }
</style>
</head>
<body>
<main class="canvas">
  <section class="card card-front" aria-label="Business card front">
    <div class="wordmark"><span class="wordmark-dot"></span><span>PELDRAX</span></div>
    <p class="front-url">www.peldrax.com</p>
  </section>

  <section class="card card-back" aria-label="Business card back">
    <svg class="swoosh" viewBox="0 0 664 380" aria-hidden="true">
      <path d="M0,362 C260,392 500,345 664,262 L664,380 L0,380 Z" fill="var(--brand-blue-light)"/>
      <path d="M0,367 C270,392 510,348 664,268" fill="none" stroke="#ffffff" stroke-width="3"/>
      <path d="M250,380 C450,372 580,320 664,274 L664,380 Z" fill="var(--brand-blue)"/>
    </svg>

    <div class="wordmark"><span class="wordmark-dot"></span><span>PELDRAX</span></div>

    <div class="person">
      <p class="person-name">TOMAS KELLER</p>
      <p class="person-title">Design Consultant</p>
    </div>

    <div class="divider"></div>

    <ul class="contact-list">
      <li>
        <svg class="contact-icon" viewBox="0 0 12 12" aria-hidden="true"><path d="M2.5 1 L4.5 1 L5.2 3.6 L4 4.6 C4.6 6 5.9 7.4 7.4 8 L8.4 6.8 L11 7.5 L11 9.5 C11 10.3 10.3 11 9.5 11 C5 11 1 7 1 2.5 C1 1.7 1.7 1 2.5 1 Z" fill="var(--brand-blue)"/></svg>
        <span>555.014.2290</span>
      </li>
      <li>
        <svg class="contact-icon" viewBox="0 0 12 12" aria-hidden="true"><rect x="1" y="2.5" width="10" height="7" fill="none" stroke="var(--brand-blue)" stroke-width="1.2"/><path d="M1 2.5 L6 6.5 L11 2.5" fill="none" stroke="var(--brand-blue)" stroke-width="1.2"/></svg>
        <span>nina@HarbrookLine.com</span>
      </li>
      <li>
        <svg class="contact-icon" viewBox="0 0 12 12" aria-hidden="true"><circle cx="6" cy="6" r="5" fill="none" stroke="var(--brand-blue)" stroke-width="1.1"/><ellipse cx="6" cy="6" rx="2.2" ry="5" fill="none" stroke="var(--brand-blue)" stroke-width="1"/><path d="M1 6 H11" stroke="var(--brand-blue)" stroke-width="1"/></svg>
        <span>www.HarbrookLine.com</span>
      </li>
    </ul>
  </section>
</main>
</body>
</html>
```